Letterhead and envelope design

Using current logo and colours I would like to have a new design done for a stationary set to be printed.

The new files should include logo, web and email address as well as,mailing address and phone number

Dov Harmsby
Harmsby Construction Inc
Box 27 Site 18 RR5
Okotoks AB
T4K 2B9
Cell : 403-555-2917
Email: dov@harmsbyconstruction.example
web: harmsbyconstruction.example

```html
<!DOCTYPE html>
<html lang="en">
<head>
<meta charset="utf-8">
<title>Harmsby Construction Stationery</title>
<link href="https://fonts.googleapis.com/css2?family=Roboto:wght@400;500&family=Pinyon+Script&display=swap" rel="stylesheet">
<style>
  :root {
    --navy: #0d2c5c;
    --orange: #d88b1f;
    --paper: #ededec;
    --ink: #2b2b2b;
    --muted: #5e5e5e;
    --backdrop: #9c9c9c;
    --faint: rgba(13, 44, 92, 0.06);
  }
  * { box-sizing: border-box; margin: 0; padding: 0; }
  html, body { width: 1200px; height: 1011px; overflow: hidden; }
  body {
    background: var(--backdrop);
    font-family: "Roboto", Arial, sans-serif;
    position: relative;
    color: var(--ink);
  }
  .sheet {
    position: absolute;
    background: var(--paper);
    overflow: hidden;
    box-shadow: 0 1px 4px rgba(0,0,0,0.25);
  }
  .letterhead { left: 85px; top: 150px; width: 509px; height: 718px; }
  .envelope-back { left: 633px; top: 351px; width: 509px; height: 241px; }
  .envelope-front { left: 633px; top: 627px; width: 509px; height: 241px; }

  .brand { position: absolute; display: flex; align-items: center; gap: 9px; }
  .brand-dot { border-radius: 50%; background: var(--navy); flex: none; }
  .brand-name {
    font-size: 11px; font-weight: 500; color: var(--navy);
    line-height: 1.15; letter-spacing: 0.2px; text-transform: uppercase;
  }
  .letterhead .brand { left: 39px; top: 21px; }
  .letterhead .brand-dot { width: 53px; height: 53px; }
  .envelope-front .brand { left: 36px; top: 32px; }
  .envelope-front .brand-dot { width: 54px; height: 54px; }

  .contact { position: absolute; display: flex; font-size: 8.3px; color: var(--muted); line-height: 10px; }
  .contact-address { text-align: right; padding-right: 10px; border-right: 1px solid #8b8b8b; }
  .contact-lines { padding-left: 11px; }
  .contact-lines div { display: flex; align-items: center; gap: 5px; }
  .contact-lines svg { width: 6px; height: 6px; flex: none; }
  .letterhead .contact { right: 38px; top: 34px; }
  .envelope-front .contact { left: 35px; top: 183px; font-size: 7.6px; }
  .envelope-front .contact-address { text-align: left; }

  .letter { position: absolute; left: 54px; top: 172px; width: 400px; font-size: 8.4px; line-height: 12px; color: var(--ink); }
  .letter p { margin-bottom: 12px; text-align: justify; }
  .letter .address { text-align: left; margin-bottom: 18px; }
  .letter .date { margin-bottom: 12px; }
  .signoff { margin-top: 38px; }
  .signature { font-family: "Pinyon Script", cursive; font-size: 16px; color: var(--ink); margin-top: 0; }

  .faint-circle { position: absolute; border-radius: 50%; background: var(--faint); }
  .letterhead .faint-circle { left: 272px; top: 499px; width: 240px; height: 240px; }
  .envelope-front .faint-circle { left: 357px; top: 95px; width: 170px; height: 170px; }

  .band { position: absolute; left: 0; bottom: 0; width: 100%; }
  .letterhead .band { height: 11px; }
  .envelope-front .band { height: 8px; }

  .flap { position: absolute; left: 0; top: 0; width: 509px; height: 241px; }
  .envelope-back .brand-dot { position: absolute; left: 232px; top: 17px; width: 44px; height: 44px; }
</style>
</head>
<body>

<section class="sheet letterhead">
  <div class="faint-circle"></div>
  <header class="brand">
    <span class="brand-dot"></span>
    <span class="brand-name">Harmsby<br>Construction</span>
  </header>
  <div class="contact">
    <div class="contact-address">Harmsby Construction Inc<br>123 Example Road<br>Sampletown AB A1A 1A1</div>
    <div class="contact-lines">
      <div><svg viewBox="0 0 6 6"><rect x="1.3" y="0.3" width="3.4" height="5.4" rx="0.6" fill="none" stroke="#0d2c5c" stroke-width="0.8"/></svg>403-555-2917</div>
      <div><svg viewBox="0 0 6 6"><rect x="0.4" y="1" width="5.2" height="4" fill="none" stroke="#0d2c5c" stroke-width="0.7"/><path d="M0.4 1 L3 3.2 L5.6 1" fill="none" stroke="#0d2c5c" stroke-width="0.7"/></svg>dov@harmsbyconstruction.example</div>
      <div><svg viewBox="0 0 6 6"><circle cx="3" cy="3" r="2.6" fill="#0d2c5c"/><path d="M0.5 3 H5.5 M3 0.4 V5.6" stroke="#ededec" stroke-width="0.5"/></svg>harmsbyconstruction.example</div>
    </div>
  </div>

  <article class="letter">
    <p class="date">01 January 2050</p>
    <p class="address">Company (Pvt) Ltd.<br>PO Box 3355 Mainville St<br>Sample City Country 3355</p>
    <p>Dear Mara Quillen,</p>
    <p>Lorem ipsum dolor sit amet, consectetuer adipiscing elit, sed diam nonummy nibh euismod tincidunt ut laoreet dolore magna aliquam erat volutpat. Ut wisi enim ad minim veniam, quis nostrud exerci tation ullamcorper suscipit lobortis nisl ut aliquip ex ea commodo consequat. Duis dolore te feugait nulla facilisi. Nam liber tempor cum soluta nobis eleifend option congue nihil imperdiet doming id quod mazim placerat facer possim assum. Lorem ipsum dolor sit amet, consectetuer adipiscing elit, sed diam nonummy nibh euismod tincidunt ut laoreet dolore magna aliquam erat volutpat. Ut wisi enim ad minim veniam, quis nostrud exerci tation ullamcorper suscipit lobortis nisl ut aliquip ex ea commodo consequat.</p>
    <p>Consectetuer adipiscing elit, sed diam nonummy nibh euismod tincidunt ut laoreet dolore magna aliquam erat volutpat. Ut wisi enim ad minim veniam, quis nostrud exerci tation ullamcorper suscipit lobortis nisl ut aliquip ex ea commodo consequat. Consectetuer adipiscing elit, sed diam nonummy nibh euismod tincidunt ut laoreet dolore magna aliquam erat volutpat. Ut wisi enim ad minim veniam, quis nostrud exerci tation ullamcorper suscipit lobortis nisl ut aliquip ex ea commodo consequat.</p>
    <p>Consectetuer adipiscing elit, sed diam nonummy nibh euismod tincidunt ut laoreet dolore magna aliquam erat volutpat. Ut wisi enim ad minim veniam, quis nostrud exerci tation ullamcorper suscipit lobortis nisl ut aliquip ex ea commodo consequat. Consectetuer adipiscing elit, sed diam nonummy nibh euismod tincidunt ut laoreet dolore magna aliquam erat volutpat. Ut wisi enim ad minim veniam, quis nostrud exerci tation ullamcorper suscipit lobortis nisl ut aliquip ex ea commodo consequat.</p>
    <p class="signoff">Sincerely Yours</p>
    <div class="signature">Dov Harmsby</div>
  </article>

  <svg class="band" viewBox="0 0 509 11" preserveAspectRatio="none">
    <polygon points="0,0 260,0 254,11 0,11" fill="#0d2c5c"/>
    <polygon points="263,0 509,0 509,11 257,11" fill="#d88b1f"/>
  </svg>
</section>

<section class="sheet envelope-back">
  <svg class="flap" viewBox="0 0 509 241">
    <path d="M2 12 L14 60 Q17 80 36 80 L473 80 Q492 80 495 60 L507 12" fill="none" stroke="#cfcfce" stroke-width="1.2"/>
    <path d="M14 60 Q17 80 36 80 L473 80 Q492 80 495 60 L497 236 L12 236 Z" fill="#e7e7e6" stroke="#d6d6d5" stroke-width="0.8"/>
  </svg>
  <span class="brand-dot"></span>
</section>

<section class="sheet envelope-front">
  <div class="faint-circle"></div>
  <header class="brand">
    <span class="brand-dot"></span>
    <span class="brand-name">Harmsby<br>Construction</span>
  </header>
  <div class="contact">
    <div class="contact-address">Harmsby Construction Inc<br>123 Example Road<br>Sampletown AB A1A 1A1</div>
    <div class="contact-lines">
      <div><svg viewBox="0 0 6 6"><rect x="1.3" y="0.3" width="3.4" height="5.4" rx="0.6" fill="none" stroke="#0d2c5c" stroke-width="0.8"/></svg>403-555-2917</div>
      <div><svg viewBox="0 0 6 6"><rect x="0.4" y="1" width="5.2" height="4" fill="none" stroke="#0d2c5c" stroke-width="0.7"/><path d="M0.4 1 L3 3.2 L5.6 1" fill="none" stroke="#0d2c5c" stroke-width="0.7"/></svg>dov@harmsbyconstruction.example</div>
      <div><svg viewBox="0 0 6 6"><circle cx="3" cy="3" r="2.6" fill="#0d2c5c"/><path d="M0.5 3 H5.5 M3 0.4 V5.6" stroke="#ededec" stroke-width="0.5"/></svg>harmsbyconstruction.example</div>
    </div>
  </div>
  <svg class="band" viewBox="0 0 509 8" preserveAspectRatio="none">
    <polygon points="0,0 259,0 254,8 0,8" fill="#0d2c5c"/>
    <polygon points="262,0 509,0 509,8 257,8" fill="#d88b1f"/>
  </svg>
</section>

</body>
</html>
```